Business card and Logo for a private personal training studio

We need a business card and logo for a private personal training studio.

The studios name is "Steady Your Path"
Main coloring to be a bright light blue. Looking for a crisp modern look

The front of the card is to have the

Studios name.
The Logo
Private Personal Training Studio
Mel Carver
0451 239 716

The back of the card is to have a lot of words relating to the services we offer. Please place the words vertically and horizontally using different fonts, different text sizes, different boldness and different colors to create a word picture.

Main words that need highlighting are

QVL, PILATES, BOXING, SPIN, STRENGTH, WEIGHT LOSS, BALANCE

Other words to add to the mix with less emphasis

Fitness, Conditioning, Lifestyle, Wellness, Health, Energy, Cardio, Goals, Muscle Tone, Vitality, Confidence, Attitude, Determination, Motivation, Dedication, Fun

Target Market(s)

Woman aged 30 to 60

Industry/Entity Type

Personal Trainer

Contact Information for Business Card

Steady Your Path
Mel Carver
0451 239 716

Colors
0493ce
33a6d7
85cae6

```html
<!DOCTYPE html>
<html lang="en">
<head>
<meta charset="utf-8">
<title>Steady Your Path – Business Card</title>
<link rel="stylesheet" href="https://fonts.googleapis.com/css2?family=Montserrat:wght@600;700&family=Quicksand:wght@300;400;500&display=swap">
<style>
  :root {
    --page: #eef1f3;
    --card-white: #fdfdfd;
    --blue-deep: #0493ce;
    --blue-mid: #33a6d7;
    --blue-soft: #85cae6;
    --back-top: #c9e8f3;
    --back-bottom: #a9d9ec;
    --ink: #6f767b;
    --ink-strong: #5f666b;
    --ink-light: #8a9196;
    --shadow: 0 14px 30px rgba(40, 60, 75, 0.18), 0 2px 6px rgba(40, 60, 75, 0.12);
  }
  * { box-sizing: border-box; margin: 0; padding: 0; }
  html, body {
    width: 1200px;
    height: 800px;
    overflow: hidden;
    background: var(--page);
  }
  .canvas {
    position: relative;
    width: 1200px;
    height: 800px;
    display: flex;
    align-items: center;
    justify-content: center;
    gap: 60px;
  }
  .card {
    position: relative;
    width: 510px;
    height: 292px;
    border-radius: 4px;
    overflow: hidden;
    box-shadow: var(--shadow);
  }

  /* Back of card – word picture */
  .card--back {
    background: linear-gradient(165deg, var(--back-top) 0%, var(--back-bottom) 100%);
  }
  .leaf-decoration {
    position: absolute;
    left: -40px;
    bottom: -70px;
    width: 620px;
    height: 200px;
    border-radius: 50% 50% 0 0 / 100% 100% 0 0;
    background: radial-gradient(ellipse at 40% 70%, rgba(255,255,255,0.55) 0%, rgba(255,255,255,0.25) 45%, rgba(255,255,255,0) 75%);
  }
  .back-words {
    position: absolute;
    top: 28px;
    left: 0;
    right: 0;
    text-align: center;
    color: var(--ink);
  }
  .back-words__main {
    font-family: 'Montserrat', sans-serif;
    font-weight: 700;
    font-size: 13.5px;
    letter-spacing: 0.2px;
    color: var(--ink-strong);
    margin-bottom: 8px;
  }
  .back-words__line {
    font-family: 'Quicksand', sans-serif;
    font-weight: 500;
    font-size: 14px;
    line-height: 23px;
  }
  .back-mark {
    position: absolute;
    left: 50%;
    top: 172px;
    width: 46px;
    height: 46px;
    margin-left: -23px;
    border-radius: 50%;
    background: rgba(255, 255, 255, 0.75);
  }

  /* Front of card */
  .card--front {
    background: var(--card-white);
  }
  .holder-name {
    position: absolute;
    top: 26px;
    left: 28px;
    font-family: 'Montserrat', sans-serif;
    font-weight: 700;
    font-size: 15px;
    letter-spacing: 0.5px;
    color: var(--ink-strong);
  }
  .studio-brand {
    position: absolute;
    top: 92px;
    left: 0;
    right: 0;
    display: flex;
    flex-direction: column;
    align-items: center;
  }
  .studio-brand__row {
    display: flex;
    align-items: center;
    gap: 14px;
  }
  .studio-brand__dot {
    width: 30px;
    height: 30px;
    border-radius: 50%;
    background: var(--blue-soft);
  }
  .studio-brand__name {
    font-family: 'Quicksand', sans-serif;
    font-weight: 400;
    font-size: 40px;
    letter-spacing: 0.5px;
    color: var(--blue-mid);
  }
  .studio-brand__tagline {
    margin-top: 4px;
    font-family: 'Quicksand', sans-serif;
    font-weight: 500;
    font-size: 15px;
    letter-spacing: 0.4px;
    color: var(--ink-light);
  }
  .holder-phone {
    position: absolute;
    right: 30px;
    bottom: 24px;
    font-family: 'Quicksand', sans-serif;
    font-weight: 500;
    font-size: 17px;
    letter-spacing: 1px;
    color: var(--ink);
  }
</style>
</head>
<body>
  <main class="canvas">
    <section class="card card--back" aria-label="Back of business card">
      <div class="leaf-decoration" role="img" aria-label="Large pale feather-leaf decoration sweeping across the card"></div>
      <div class="back-words">
        <p class="back-words__main">QVL, PILATES, BOXING, SPIN, STRENGTH, WEIGHT LOSS, BALANCE</p>
        <p class="back-words__line">Fitness, Conditioning, Lifestyle, Wellness, Health, Energy</p>
        <p class="back-words__line">Cardio, Goals, Muscle Tone, Vitality, Confidence</p>
        <p class="back-words__line">Attitude, Determination, Motivation</p>
        <p class="back-words__line">Dedication, Fun</p>
      </div>
      <div class="back-mark" aria-hidden="true"></div>
    </section>

    <section class="card card--front" aria-label="Front of business card">
      <p class="holder-name">MEL CARVER</p>
      <div class="studio-brand">
        <div class="studio-brand__row">
          <span class="studio-brand__dot" aria-hidden="true"></span>
          <h1 class="studio-brand__name">Steady Your Path</h1>
        </div>
        <p class="studio-brand__tagline">Private Personal Training Studio</p>
      </div>
      <p class="holder-phone">0451 239 716</p>
    </section>
  </main>
</body>
</html>
```